Northpeak Medical Billing needs a business card design

We need a business card design for a medical billing service, located in Anchorage, AK. We provide medical claims billing and management to Alaskan medical practices/clinics. We would like to see designs that depict Alaskan Mountain Ranges, or water features, or trees. An outdoorsy feel, perhaps. Not exactly sure.

Industry/Entity Type

Medical

```html
<!DOCTYPE html>
<html lang="en">
<head>
<meta charset="utf-8">
<title>Northpeak Medical Billing – Business Card</title>
<link rel="stylesheet" href="https://fonts.googleapis.com/css2?family=Exo+2:wght@600;700&family=Open+Sans:wght@400;600&display=swap">
<style>
  :root {
    --page-bg: #e9e6e1;
    --card-white: #ffffff;
    --brand-blue: #1c5fa6;
    --deep-blue: #0f4a8c;
    --mid-blue: #2474c2;
    --accent-sky: #3bb3e6;
    --text-light: #ffffff;
    --text-soft: #d7e6f6;
  }
  html, body {
    margin: 0;
    padding: 0;
    width: 1200px;
    height: 1023px;
    overflow: hidden;
    background: var(--page-bg);
  }
  .canvas {
    position: relative;
    width: 1200px;
    height: 1023px;
  }
  .business-card {
    position: absolute;
    left: 170px;
    top: 261px;
    width: 860px;
    height: 500px;
    background: var(--card-white);
    box-shadow: 0 14px 40px rgba(0, 0, 0, 0.25);
    overflow: hidden;
  }
  .card-waves {
    position: absolute;
    inset: 0;
    width: 860px;
    height: 500px;
  }
  .brand {
    position: absolute;
    left: 56px;
    top: 196px;
    display: flex;
    align-items: center;
    gap: 18px;
  }
  .brand-square {
    width: 26px;
    height: 26px;
    background: var(--brand-blue);
  }
  .brand-name {
    font-family: "Open Sans", sans-serif;
    font-weight: 600;
    font-size: 30px;
    line-height: 1.15;
    color: var(--brand-blue);
    letter-spacing: 1px;
  }
  .contact {
    position: absolute;
    right: 52px;
    top: 62px;
    text-align: right;
    color: var(--text-light);
    font-family: "Open Sans", sans-serif;
  }
  .person-name {
    font-family: "Exo 2", sans-serif;
    font-weight: 700;
    font-size: 40px;
    letter-spacing: 2px;
    margin: 0;
    text-transform: uppercase;
  }
  .person-title {
    font-size: 20px;
    color: var(--text-soft);
    margin: 2px 0 30px;
  }
  .contact-line {
    display: flex;
    justify-content: flex-end;
    align-items: center;
    gap: 10px;
    font-size: 21px;
    margin: 4px 0;
  }
  .contact-icon {
    width: 20px;
    height: 20px;
    border-radius: 3px;
    background: var(--accent-sky);
    display: inline-flex;
    align-items: center;
    justify-content: center;
  }
  .address {
    margin-top: 26px;
    font-size: 21px;
    line-height: 1.4;
  }
</style>
</head>
<body>
<main class="canvas">
  <section class="business-card">
    <svg class="card-waves" viewBox="0 0 860 500" aria-hidden="true">
      <defs>
        <linearGradient id="panelGradient" x1="0" y1="0" x2="1" y2="1">
          <stop offset="0" stop-color="#2a7ccb"/>
          <stop offset="1" stop-color="#0f4a8c"/>
        </linearGradient>
      </defs>
      <path d="M458 0 C 376 180, 436 330, 314 500 L860 500 L860 0 Z" fill="#3bb3e6"/>
      <path d="M486 0 C 404 180, 464 330, 342 500 L860 500 L860 0 Z" fill="url(#panelGradient)"/>
    </svg>

    <div class="brand">
      <div class="brand-square"></div>
      <div class="brand-name">NORTHPEAK<br>MEDICAL BILLING</div>
    </div>

    <div class="contact">
      <h1 class="person-name">Daniel R. Hale</h1>
      <p class="person-title">Director</p>
      <div class="contact-line">
        <span>(907) 555-0142</span>
        <span class="contact-icon">
          <svg width="12" height="12" viewBox="0 0 24 24"><path fill="#fff" d="M6.6 10.8a15 15 0 0 0 6.6 6.6l2.2-2.2a1 1 0 0 1 1-.25 11.4 11.4 0 0 0 3.6.57 1 1 0 0 1 1 1V20a1 1 0 0 1-1 1A17 17 0 0 1 3 4a1 1 0 0 1 1-1h3.5a1 1 0 0 1 1 1c0 1.25.2 2.45.57 3.57a1 1 0 0 1-.25 1z"/></svg>
        </span>
      </div>
      <div class="contact-line">
        <span>(907) 555-0187</span>
        <span class="contact-icon">
          <svg width="12" height="12" viewBox="0 0 24 24"><rect x="3" y="8" width="18" height="10" fill="#fff"/><rect x="7" y="3" width="10" height="5" fill="#fff"/></svg>
        </span>
      </div>
      <div class="contact-line">
        <span>info@northpeakbilling.com</span>
        <span class="contact-icon">
          <svg width="12" height="12" viewBox="0 0 24 24"><rect x="2" y="5" width="20" height="14" fill="#fff"/><path d="M2 5l10 8 10-8" stroke="#3bb3e6" stroke-width="2" fill="none"/></svg>
        </span>
      </div>
      <p class="address">214 Harbor Lane<br>Anchorage, AK 99501</p>
    </div>
  </section>
</main>
</body>
</html>
```